Supplement business needs a label design

We need a label design for our company KALVANTE LLC in The Woodlands, Texas,
This label is for a Fish Oil supplement.
Here is the task:
1. The text needs to be bold and readable on smartphone ads
2. The background is in a basic standard color like blue, silver, black, brown, etc
3. A watermark is on the background-color (waves, leaves, etc.).
4. The Brand will be "K A L V A N T E" with the attached logo design and "CU T T I N G E D G E F O R MU L A SU P P L E M E N T " :
5. Further details have to be on the label like on the attached Fish oil sample: "450 E P A / 300 D H A 1 , 2 5 0 M G DIETARY SUPPLEMENT GLUTENFREE with the icon and heart icon.
6. Please see attached samples:

```html
<!DOCTYPE html>
<html lang="en">
<head>
<meta charset="utf-8">
<title>KALVANTE Fish Oil Label</title>
<link href="https://fonts.googleapis.com/css2?family=Montserrat:wght@600;800&family=Oswald:wght@500;600&display=swap" rel="stylesheet">
<style>
  :root {
    --stage-dark: #02050d;
    --stage-glow: #0a2c63;
    --navy: #28266d;
    --blue-strong: #1d5fc9;
    --blue-mid: #3f8fe0;
    --blue-light: #a9d6fa;
    --paper: #ffffff;
    --ink: #232323;
  }
  html, body {
    margin: 0;
    width: 1200px;
    height: 1156px;
    overflow: hidden;
  }
  body {
    background: radial-gradient(ellipse at 50% 50%, var(--stage-glow) 0%, var(--stage-dark) 70%);
  }
  .label {
    position: absolute;
    left: 140px;
    top: 58px;
    width: 920px;
    height: 1040px;
    display: block;
  }
  .tagline {
    font-family: "Oswald", sans-serif;
    font-weight: 500;
    font-size: 50px;
    fill: var(--paper);
  }
  .brand-name {
    font-family: "Montserrat", sans-serif;
    font-weight: 600;
    font-size: 74px;
    fill: var(--ink);
  }
  .product-name {
    font-family: "Montserrat", sans-serif;
    font-weight: 800;
    font-size: 168px;
    fill: var(--paper);
  }
  .potency {
    font-family: "Oswald", sans-serif;
    font-weight: 600;
    font-size: 40px;
    fill: var(--navy);
  }
  .category {
    font-family: "Oswald", sans-serif;
    font-weight: 500;
    font-size: 30px;
    fill: var(--navy);
  }
</style>
</head>
<body>
<svg class="label" viewBox="0 0 920 1040" xmlns="http://www.w3.org/2000/svg">
  <defs>
    <linearGradient id="sea" x1="0" y1="0" x2="0" y2="1">
      <stop offset="0" stop-color="var(--blue-strong)"/>
      <stop offset="0.45" stop-color="var(--blue-mid)"/>
      <stop offset="1" stop-color="var(--blue-light)"/>
    </linearGradient>
  </defs>

  <rect class="label-paper" width="920" height="1040" fill="var(--paper)"/>

  <!-- lower wave field -->
  <path class="wave-field" d="M0 420 C300 400 600 430 920 490 V1005 H0 Z" fill="url(#sea)"/>
  <path class="wave-line" d="M0 600 C250 540 600 560 920 680" stroke="var(--paper)" stroke-width="14" fill="none" opacity="0.55"/>
  <path class="wave-line" d="M0 980 C300 760 640 760 920 860" stroke="var(--paper)" stroke-width="40" fill="none" opacity="0.7"/>
  <path class="wave-line" d="M0 1000 C320 820 620 830 920 920" stroke="var(--navy)" stroke-width="10" fill="none" opacity="0.5"/>
  <path class="wave-line" d="M120 720 C380 660 640 690 920 760" stroke="var(--paper)" stroke-width="6" fill="none" opacity="0.6"/>

  <!-- navy band -->
  <path class="band" d="M0 370 C300 350 620 390 920 440 V500 C620 440 300 410 0 440 Z" fill="var(--navy)"/>

  <!-- top right swoosh -->
  <path class="swoosh" d="M0 0 H920 V450 C760 390 560 230 320 80 C210 20 90 20 0 55 Z" fill="var(--navy)"/>
  <path class="swoosh-cut" d="M0 55 C90 20 210 20 320 80 C470 170 560 260 640 330 C420 180 200 120 0 150 Z" fill="var(--paper)"/>

  <text class="tagline" text-anchor="end">
    <tspan x="902" y="120">CUTTING EDGE</tspan>
    <tspan x="902" y="178">FORMULA</tspan>
    <tspan x="902" y="236">SUPPLEMENT</tspan>
  </text>

  <!-- brand -->
  <circle class="brand-dot" cx="72" cy="268" r="34" fill="var(--navy)"/>
  <text class="brand-name" x="128" y="294">KALVANTE</text>

  <!-- product -->
  <text class="product-name" x="478" y="668" text-anchor="middle" textLength="660" lengthAdjust="spacingAndGlyphs">FISH OIL</text>
  <text class="potency" x="478" y="756" text-anchor="middle" textLength="600" lengthAdjust="spacing">450 E P A / 300 D H A 1 , 2 5 0 M G</text>
  <text class="category" x="478" y="822" text-anchor="middle" textLength="396" lengthAdjust="spacing">DIETARY SUPPLEMENT</text>

  <!-- quality badge, plain shape -->
  <circle class="quality-badge" cx="150" cy="912" r="70" fill="var(--paper)" stroke="var(--navy)" stroke-width="10"/>

  <!-- gluten free badge, plain shape -->
  <circle class="badge" cx="834" cy="916" r="78" fill="var(--paper)" stroke="var(--navy)" stroke-width="8"/>

  <rect class="base-strip" x="0" y="1003" width="920" height="37" fill="var(--navy)"/>
</svg>
</body>
</html>
```